Postcard Design

We need a postcard design size DL, front and back in colour, for a Excavation and Earthmoving company specialising in residential jobs including landscaping, drainage, pool excavations and fill ins, footings, trenching, driveways, retaining walls and after build clean ups
using images from out facebook page https://www.pictoralbum.example/7304918265530471/photos/pb.7304918265530471.-4819270000.8836102457./9052837164028391/?type=3&theater

```html
<!DOCTYPE html>
<html lang="en">
<head>
<meta charset="utf-8">
<title>Burrow Bros Earthworks – DL Postcard</title>
<link rel="stylesheet" href="https://fonts.googleapis.com/css2?family=Bebas+Neue&family=Lato:ital,wght@0,400;0,700;0,900;1,400;1,700&display=swap">
<style>
  :root{
    --green:#2eb41a;
    --green-dark:#239a12;
    --charcoal:#262626;
    --charcoal-light:#464646;
    --grey-light:#f4f4f4;
    --grey-mid:#cfcfcf;
    --ink:#333333;
    --white:#ffffff;
    --page:#ececec;
    --stamp:#dcdcdc;
  }
  *{box-sizing:border-box;margin:0;padding:0}
  html,body{width:825px;height:1200px;overflow:hidden;background:var(--page)}
  .canvas{position:relative;width:825px;height:1200px}
  .postcard{position:absolute;left:59px;width:708px;height:333px;overflow:hidden;background:var(--white);box-shadow:0 2px 8px rgba(0,0,0,.18)}
  .postcard--front{top:246px}
  .postcard--back{top:657px}
  .shapes{position:absolute;inset:0;width:708px;height:333px;z-index:2}
  .photo{position:absolute;z-index:1}
  .layer{position:absolute;z-index:3}

  .photo--hero{left:0;top:0;width:330px;height:182px;
    background:linear-gradient(160deg,#8fb56a 0%,#5f8f3c 45%,#d25a22 62%,#6b4b32 80%,#4f7a2f 100%)}

  .headline{right:18px;top:16px;white-space:nowrap;text-align:right;font-family:"Bebas Neue",sans-serif;font-weight:400;font-size:27px;color:var(--white);letter-spacing:.2px;line-height:1}
  .intro{left:378px;top:76px;width:308px;text-align:right;font-family:"Lato",sans-serif;font-style:italic;font-size:16px;line-height:20px;color:var(--ink)}
  .intro strong{color:var(--green);font-weight:700}

  .photo-pair{left:421px;top:147px;width:265px;height:70px;border:2px solid var(--green);background:var(--white);display:flex;gap:3px;padding:2px}
  .photo-pair .photo{position:static;flex:1;height:100%}
  .photo--loader{background:linear-gradient(135deg,#7fae55 0%,#c9a423 50%,#5d8d3a 100%)}
  .photo--truck{background:linear-gradient(135deg,#b9c8a4 0%,#eeeeee 50%,#c85a28 100%)}

  .brand{display:flex;align-items:center;gap:8px;font-family:"Lato",sans-serif;font-weight:900;color:var(--green);line-height:1.05}
  .brand__dot{width:14px;height:14px;border-radius:50%;background:var(--charcoal);flex:none}
  .brand--front{left:470px;top:238px;font-size:22px}
  .brand--back{left:22px;top:22px;font-size:17px}

  .services{left:20px;top:204px;display:grid;grid-template-columns:166px 190px;row-gap:1px;list-style:none;font-family:"Lato",sans-serif;font-style:italic;font-size:16.5px;color:var(--white);line-height:20px}
  .services li{position:relative;padding-left:15px}
  .services li::before{content:"";position:absolute;left:0;top:7px;width:7px;height:7px;border-radius:50%;background:var(--green)}

  .join-badge{width:98px;height:98px;border-radius:50%;background:var(--white);box-shadow:0 2px 5px rgba(0,0,0,.3);display:flex;align-items:center;justify-content:center}
  .join-badge__inner{width:86px;height:86px;border-radius:50%;border:4px solid var(--green);background:radial-gradient(circle at 50% 35%,#ffffff 0%,#e3e3e3 100%);display:flex;flex-direction:column;align-items:center;justify-content:center;font-family:"Bebas Neue",sans-serif;font-size:25px;line-height:.95}
  .join-badge__top{color:var(--charcoal)}
  .join-badge__bottom{color:var(--green)}
  .join-badge--front{left:304px;top:117px}
  .join-badge--back{left:317px;top:106px}

  .photo--excavator{left:196px;top:20px;width:164px;height:68px;border:2px solid var(--green);
    background:linear-gradient(120deg,#5a5a55 0%,#c8552a 40%,#8d8a83 70%,#d7d5cf 100%)}

  .feature{left:24px;top:128px;width:268px;font-family:"Lato",sans-serif;font-style:italic;font-size:12.3px;line-height:16px;color:var(--white);text-align:justify}

  .contact-title{left:22px;top:224px;font-family:"Bebas Neue",sans-serif;font-weight:400;font-size:31px;line-height:31px;color:var(--white)}
  .contact-list{left:117px;top:220px;font-family:"Bebas Neue",sans-serif;font-size:23px;line-height:24px;color:var(--white);letter-spacing:.4px}
  .contact-list .name{color:var(--green)}
  .contact-list .web{font-family:"Lato",sans-serif;font-size:17.5px;letter-spacing:0;line-height:24px}

  .stamp-box{left:633px;top:18px;width:56px;height:56px;background:var(--stamp)}
</style>
</head>
<body>
<main class="canvas">

  <section class="postcard postcard--front">
    <div class="photo photo--hero" role="img" aria-label="Orange mini excavator lifting a tree stump on a green lawn"></div>

    <svg class="shapes" viewBox="0 0 708 333" aria-hidden="true">
      <defs>
        <linearGradient id="frontPanel" x1="0" y1="0" x2="0" y2="1">
          <stop offset="0" stop-color="#fbfbfb"/>
          <stop offset="1" stop-color="#cdcdcd"/>
        </linearGradient>
        <linearGradient id="frontDark" x1="0" y1="0" x2="0" y2="1">
          <stop offset="0" stop-color="#222"/>
          <stop offset="1" stop-color="#474747"/>
        </linearGradient>
      </defs>
      <polygon points="296,0 708,0 708,302 420,302" fill="url(#frontPanel)"/>
      <polygon points="290,0 298,0 420,302 412,302" fill="#ffffff"/>
      <polygon points="298,0 306,0 428,302 420,302" fill="var(--green)"/>
      <polygon points="300,0 708,0 708,56 323,56" fill="var(--green)"/>
      <polygon points="326,60 708,60 708,67 329,67" fill="var(--charcoal)"/>
      <polygon points="0,182 372,182 375,190 0,190" fill="var(--green)"/>
      <polygon points="0,190 366,190 412,302 0,302" fill="url(#frontDark)"/>
      <rect x="0" y="302" width="708" height="31" fill="var(--green)"/>
    </svg>

    <h1 class="layer headline">A Locally Owned &amp; Operated Business</h1>
    <p class="layer intro"><strong>Burrow Bros Earthworks</strong> is a Excavation and Earthmoving company specialising in tight access earthmoving &amp; excavation.</p>

    <div class="layer photo-pair">
      <div class="photo photo--loader" role="img" aria-label="Compact track loader with bucket on grass"></div>
      <div class="photo photo--truck" role="img" aria-label="White tipper truck carrying the mini excavator"></div>
    </div>

    <div class="layer brand brand--front"><span class="brand__dot"></span><span>Burrow Bros<br>Earthworks</span></div>

    <ul class="layer services">
      <li>Landscaping</li><li>Trenching</li>
      <li>Drainage</li><li>Driveways</li>
      <li>Pool excavations</li><li>Retaining walls</li>
      <li>Fill ins &amp; footings</li><li>After build clean ups</li>
    </ul>

    <div class="layer join-badge join-badge--front">
      <div class="join-badge__inner"><span class="join-badge__top">Join us</span><span class="join-badge__bottom">Today!</span></div>
    </div>
  </section>

  <section class="postcard postcard--back">
    <svg class="shapes" viewBox="0 0 708 333" aria-hidden="true">
      <defs>
        <linearGradient id="backPanel" x1="0" y1="0" x2="1" y2="1">
          <stop offset="0" stop-color="#fafafa"/>
          <stop offset="1" stop-color="#cfcfcf"/>
        </linearGradient>
        <linearGradient id="backDark" x1="0" y1="0" x2="0" y2="1">
          <stop offset="0" stop-color="#222"/>
          <stop offset="1" stop-color="#474747"/>
        </linearGradient>
      </defs>
      <polygon points="0,0 380,0 361,110 0,110" fill="url(#backPanel)"/>
      <polygon points="0,110 361,110 345,207 0,207" fill="var(--green)"/>
      <polygon points="0,207 345,207 329,301 0,301" fill="url(#backDark)"/>
      <polygon points="380,0 388,0 337,301 329,301" fill="var(--green)"/>
      <rect x="0" y="301" width="708" height="32" fill="var(--green)"/>
    </svg>

    <div class="layer brand brand--back"><span class="brand__dot"></span><span>Burrow Bros<br>Earthworks</span></div>
    <div class="photo layer photo--excavator" role="img" aria-label="Orange mini excavator parked in a shed"></div>

    <p class="layer feature">Our mini excavator is capable of going through 760mm gaps which seperates us from our competitiors, we can fit though gates, doors and most foot paths.</p>

    <div class="layer join-badge join-badge--back">
      <div class="join-badge__inner"><span class="join-badge__top">Join us</span><span class="join-badge__bottom">Today!</span></div>
    </div>

    <h2 class="layer contact-title">Contact<br>Us Now!</h2>
    <div class="layer contact-list">
      <div><span class="name">Marco</span> : 0400612947</div>
      <div><span class="name">Tobias</span> : 0408735160</div>
      <div class="web">burrowbrosearth.example</div>
    </div>

    <div class="layer stamp-box" aria-label="Stamp area"></div>
  </section>

</main>
</body>
</html>
```